Popup Banners - BrightCounsel - Legal Technology

- We need two banners (same style) designed with two different images and different text.

- The details of the printing requirements are attached, along with suggested images.

- The banners should share the same theme as our website www.brightcounsel.com.au

- The first banner would include our logo (attached), use the 'roads join' image (attached) in some way and text: New Opportunities - Where legal services and technology meet.

- The second banner would include our logo (attached), use the 'jigsaw' image (attached) in some way and use text: Legal Technology Strategy, Advice and Capability.

- Details on what are required from the Printer is attached also.

Target Market(s)

Legal Professionals

Industry/Entity Type

Information Technology

Font styles to use
Sans Serif

Requirements
Must have
• Our logo (attached), suggested text and the image mentioned for each.
Nice to have
• Professional and modern look
Should not have
• Cheap looking

```html
<!DOCTYPE html>
<html lang="en">
<head>
<meta charset="utf-8">
<title>BrightCounsel – Pull-up Banner</title>
<link rel="stylesheet" href="https://fonts.googleapis.com/css2?family=Fira+Sans:wght@400;600;700&family=PT+Sans+Narrow&display=swap">
<style>
  :root {
    --stage: #2a2c30;
    --white: #ffffff;
    --ink: #161616;
    --ink-warm: #4b4543;
    --taupe: #756b66;
    --taupe-dark: #5c5450;
    --navy: #0f2a45;
    --navy-deep: #0b1d31;
    --steel: #3b5570;
    --glow: #b9d6ee;
    --accent-blue: #4a9fd8;
    --icon-line: #55575b;
  }
  * { box-sizing: border-box; margin: 0; padding: 0; }
  html, body { width: 1200px; height: 1200px; overflow: hidden; }
  body {
    background: var(--stage);
    font-family: "Fira Sans", sans-serif;
    position: relative;
  }
  .banner {
    position: absolute;
    left: 373px; top: 40px;
    width: 454px; height: 1120px;
    background: var(--white);
    display: flex; flex-direction: column;
  }
  .brand-bar {
    height: 129px;
    display: flex; align-items: center; justify-content: center; gap: 14px;
  }
  .brand-mark {
    width: 26px; height: 26px; background: var(--accent-blue);
  }
  .brand-name {
    font-family: "Fira Sans", sans-serif;
    font-weight: 400;
    font-size: 34px;
    letter-spacing: 5px;
    color: var(--ink-warm);
  }
  .hero {
    position: relative;
    height: 301px;
    background:
      radial-gradient(ellipse 38% 42% at 62% 48%, rgba(235,245,255,.95) 0%, rgba(185,214,238,.6) 35%, rgba(59,85,112,0) 75%),
      linear-gradient(135deg, #2a4862 0%, #1b3852 45%, #0f2a45 100%);
    overflow: hidden;
  }
  .url-tab {
    position: absolute;
    left: 75px; bottom: 0;
    width: 306px; height: 46px;
    border-radius: 10px 10px 0 0;
    background: linear-gradient(180deg, #8a807a 0%, var(--taupe) 55%, var(--taupe-dark) 100%);
    color: var(--white);
    font-family: "PT Sans Narrow", sans-serif;
    font-size: 30px;
    display: flex; align-items: center; justify-content: center;
  }
  .headline {
    height: 222px;
    display: flex; align-items: center; justify-content: center;
    text-align: center;
    font-weight: 700;
    font-size: 28px;
    line-height: 37px;
    letter-spacing: 3.5px;
    color: var(--ink);
    text-transform: uppercase;
  }
  .services {
    position: relative;
    height: 302px;
    background:
      radial-gradient(ellipse 45% 35% at 45% 55%, rgba(120,135,155,.45) 0%, rgba(21,37,56,0) 80%),
      linear-gradient(160deg, #2c3a4e 0%, #1a2b40 50%, var(--navy-deep) 100%);
  }
  .service {
    position: absolute;
    width: 210px;
    display: flex; flex-direction: column; align-items: center;
  }
  .service-icon {
    width: 73px; height: 73px; border-radius: 50%;
    background: var(--white);
    display: flex; align-items: center; justify-content: center;
  }
  .service-icon svg { width: 40px; height: 40px; fill: none; stroke: var(--icon-line); stroke-width: 2; stroke-linejoin: round; stroke-linecap: round; }
  .service-label {
    margin-top: 18px;
    color: var(--white);
    font-weight: 600;
    font-size: 16.5px;
    letter-spacing: .4px;
    text-transform: uppercase;
    white-space: nowrap;
  }
  .service--established { left: 8px;   top: 30px; }
  .service--automation  { left: 226px; top: 30px; }
  .service--review      { left: 8px;   top: 166px; }
  .service--research    { left: 226px; top: 166px; }
  .contact {
    height: 102px;
    display: flex; align-items: center; justify-content: center; gap: 12px;
    color: var(--ink-warm);
    font-weight: 700;
    font-size: 37px;
    letter-spacing: 4px;
  }
  .contact svg { width: 22px; height: 28px; fill: none; stroke: var(--ink-warm); stroke-width: 3; stroke-linecap: round; }
  .base {
    position: relative;
    flex: 1;
    background: var(--navy);
  }
  .base-rule {
    position: absolute;
    left: 67px; top: 0;
    width: 320px; height: 13px;
    background: var(--taupe-dark);
  }
</style>
</head>
<body>
  <main class="banner">
    <header class="brand-bar">
      <span class="brand-mark"></span>
      <span class="brand-name">BrightCounsel</span>
    </header>

    <section class="hero" role="img" aria-label="Photo of a hand placing a glowing jigsaw piece into a blue puzzle">
      <div class="url-tab">brightcounsel.com.au</div>
    </section>

    <h1 class="headline">Legal Technology<br>Strategy, Advice<br>and Capability</h1>

    <section class="services" role="img" aria-label="Faded blue jigsaw puzzle photo behind service icons">
      <div class="service service--established">
        <div class="service-icon">
          <svg viewBox="0 0 40 40"><path d="M10 6v30"/><path d="M10 8h20l-5 7 5 7H10"/></svg>
        </div>
        <div class="service-label">Established</div>
      </div>
      <div class="service service--automation">
        <div class="service-icon">
          <svg viewBox="0 0 40 40"><rect x="5" y="8" width="30" height="20" rx="1"/><path d="M16 34h8M20 28v6"/><path d="M10 23l6-6 4 3 7-7"/></svg>
        </div>
        <div class="service-label">Process Automation</div>
      </div>
      <div class="service service--review">
        <div class="service-icon">
          <svg viewBox="0 0 40 40"><path d="M9 12h7a4 4 0 1 1 8 0h7v9a4 4 0 1 0 0 8v5H9v-7a4 4 0 1 0 0-8z"/></svg>
        </div>
        <div class="service-label">Strategic Review</div>
      </div>
      <div class="service service--research">
        <div class="service-icon">
          <svg viewBox="0 0 40 40"><path d="M4 8h5l4 18h19l3-13H11"/><circle cx="15" cy="31" r="2.5"/><circle cx="29" cy="31" r="2.5"/></svg>
        </div>
        <div class="service-label">Industry Research</div>
      </div>
    </section>

    <footer class="contact">
      <svg viewBox="0 0 22 28"><path d="M7 3l-3 3c-2 5 3 15 9 19l3-3"/></svg>
      <span class="phone">07 3000 0199</span>
    </footer>

    <div class="base"><span class="base-rule"></span></div>
  </main>
</body>
</html>
```